Business Card Design Project Bright Way

Simple and clean business card,

Logo and fond added in attachment

Data need to be changable:
Lien Varmeko
Customer Service Specialist

Bright Way - lien.varmeko@brightway-mail.be - Mob: +32471538046 - www.brightway-mail.be

Target Market(s)

Small businesses

Industry/Entity Type

Business

Requirements
Nice to have
• QR-code

```html
<!DOCTYPE html>
<html lang="en">
<head>
<meta charset="utf-8">
<title>Bright Way – Business Card</title>
<link href="https://fonts.googleapis.com/css2?family=Mulish:wght@400;600;700&display=swap" rel="stylesheet">
<style>
  :root {
    --backdrop: #3a3a3a;
    --card: #ececec;
    --accent-green: #7cc242;
    --accent-blue: #29a8e0;
    --ink: #1f1f1f;
    --ink-soft: #3c3c3c;
  }
  * { box-sizing: border-box; margin: 0; padding: 0; }
  html, body {
    width: 1200px; height: 799px; overflow: hidden;
    background: var(--backdrop);
    font-family: "Mulish", sans-serif;
  }
  .canvas {
    width: 1200px; height: 799px;
    display: flex; align-items: center; justify-content: center;
  }
  .card {
    position: relative;
    width: 900px; height: 582px;
    background: var(--card);
    box-shadow: 0 14px 40px rgba(0,0,0,.45);
  }
  .edge-bar {
    position: absolute; width: 14px;
    background: var(--accent-green);
  }
  .edge-bar--left { left: 0; top: 60px; height: 250px; }
  .edge-bar--right { right: 0; top: 235px; height: 260px; }

  .brand {
    position: absolute; left: 300px; top: 128px;
    display: flex; align-items: center; gap: 22px;
  }
  .brand__mark {
    width: 64px; height: 64px;
    background: var(--accent-blue); border-radius: 10px;
  }
  .brand__name {
    font-weight: 600; font-size: 62px; line-height: 1;
    color: var(--accent-green); letter-spacing: 1px;
  }

  .person {
    position: absolute; right: 505px; top: 292px;
    text-align: right;
  }
  .person__name {
    font-weight: 700; font-size: 30px; color: var(--accent-blue);
  }
  .person__role {
    font-size: 17px; color: var(--ink-soft); margin-top: 4px;
  }
  .divider {
    position: absolute; left: 418px; top: 292px;
    width: 2px; height: 96px; background: var(--accent-green);
  }
  .contacts {
    position: absolute; left: 438px; top: 290px;
    list-style: none;
  }
  .contacts__item {
    display: flex; align-items: center; gap: 10px;
    font-size: 21px; color: var(--ink); height: 34px;
  }
  .contacts__icon { width: 18px; height: 18px; flex: none; }
</style>
</head>
<body>
<main class="canvas">
  <article class="card">
    <span class="edge-bar edge-bar--left"></span>
    <span class="edge-bar edge-bar--right"></span>

    <div class="brand">
      <span class="brand__mark"></span>
      <span class="brand__name">Bright Way</span>
    </div>

    <div class="person">
      <p class="person__name">Lien Varmeko</p>
      <p class="person__role">Customer Service Specialist</p>
    </div>

    <span class="divider"></span>

    <ul class="contacts">
      <li class="contacts__item">
        <svg class="contacts__icon" viewBox="0 0 18 18" fill="none" stroke="#29a8e0" stroke-width="1.4">
          <circle cx="9" cy="9" r="8"/><rect x="5" y="6" width="8" height="6"/><path d="M5 6l4 3 4-3"/>
        </svg>
        lien.varmeko@brightway-mail.be
      </li>
      <li class="contacts__item">
        <svg class="contacts__icon" viewBox="0 0 18 18" fill="none" stroke="#29a8e0" stroke-width="1.4">
          <circle cx="9" cy="9" r="8"/><path d="M6.5 5.5c0 3.5 2.5 6.5 5.5 7l1-1.6-1.8-1-1 .8c-1-.5-1.7-1.3-2.1-2.2l.8-1-1-1.8z"/>
        </svg>
        +32471538046
      </li>
      <li class="contacts__item">
        <svg class="contacts__icon" viewBox="0 0 18 18" fill="none" stroke="#29a8e0" stroke-width="1.4">
          <circle cx="9" cy="9" r="8"/><circle cx="9" cy="9" r="4.5"/><path d="M4.5 9h9M9 4.5c-2 3-2 6 0 9M9 4.5c2 3 2 6 0 9"/>
        </svg>
        www.brightway-mail.be
      </li>
    </ul>
  </article>
</main>
</body>
</html>
```